Pemberly College Graduates Society of Atlanta 148th Founders Eve Recital Celebration March 21, 2015

I need a double-sided postcard highlighting the following info with vibrant colors representing the school colors (blue, red, white): Front- the Pemberly College Graduates Society of Atlanta 2015 Founders Eve Recital featuring the Pemberly College Praise Singers. The event is March 21, 2015 at 1:00 PM and will be held at St. Oswin's Methodist Chapel: 682 Marlow Avenue, NE Atlanta, GA 30317. The event is free and open to the community. The purpose of the event is to raise funds for our Annual Scholarship Fund. Donations will be accepted at the event or Donate online at PCGSA FundRaven Scholarship Campaign: fundraven.example/qk7tzb; www.pcgradsatl.example

Back- Ideally, we saw the front being the major graphic and the back being designed postcard style for mailing. Half of the card could have the following upcoming events:

March 14: General Body Meeting

April 8-12: Springbreak Bus Trip to Pemberly College

August 15: FalconJam

Target Market(s)

ages 25-50

Industry/Entity Type

School

Font styles to use
Script

Colors
ec1f27
0455a3
ffffff
33a6d7
0692cd

Requirements
Must have
• Very vibrant with bold colors to match school colors (blue, red, white). I've attached last year program as a guidline.
Nice to have
• pictures of the university and gospel choir

```html
<!DOCTYPE html>
<html lang="en">
<head>
<meta charset="utf-8">
<title>PCGSA Postcard – Back</title>
<link rel="stylesheet" href="https://fonts.googleapis.com/css2?family=Oranienbaum&display=swap">
<style>
  :root {
    --brand-red: #ec1f27;
    --brand-blue: #0455a3;
    --event-blue: #1f3fe0;
    --paper: #ffffff;
    --ink: #111111;
  }
  * { margin: 0; padding: 0; box-sizing: border-box; }
  html, body {
    width: 1200px; height: 917px; overflow: hidden;
    background: var(--paper);
  }
  .postcard {
    position: relative;
    width: 1200px; height: 917px;
    border: 3px solid var(--ink);
    background: var(--paper);
    font-family: "Oranienbaum", "Times New Roman", serif;
  }
  .brand {
    position: absolute; left: 190px; top: 68px;
    display: flex; align-items: center; gap: 12px;
  }
  .brand-mark {
    width: 62px; height: 86px; background: var(--brand-blue);
  }
  .brand-name {
    color: var(--brand-blue);
    font-weight: 400;
    line-height: 1;
  }
  .brand-name .short { display: block; font-size: 44px; letter-spacing: 2px; }
  .brand-name .long { display: block; font-size: 19px; margin-top: 4px; }
  .brand-club {
    position: absolute; left: 205px; top: 158px;
    font-size: 11px; color: var(--brand-blue);
  }
  .stamp-box {
    position: absolute; left: 1016px; top: 68px;
    width: 85px; height: 101px;
    border: 1.5px solid var(--ink);
  }
  .divider {
    position: absolute; left: 601px; top: 185px;
    width: 3px; height: 624px; background: var(--brand-red);
  }
  .events { position: absolute; left: 102px; top: 305px; }
  .events-title {
    font-size: 46px; font-weight: 400; color: var(--event-blue);
    margin-bottom: 62px;
  }
  .event-list { list-style: none; }
  .event {
    display: flex; font-size: 32px; line-height: 36px;
    margin-bottom: 36px;
  }
  .event-date { color: var(--brand-red); white-space: pre; }
  .event-name { color: var(--event-blue); }
  .address-lines { position: absolute; left: 688px; top: 440px; }
  .address-line {
    width: 410px; height: 2px; background: var(--ink);
    margin-bottom: 59px;
  }
</style>
</head>
<body>
  <main class="postcard">
    <header class="brand">
      <div class="brand-mark"></div>
      <div class="brand-name">
        <span class="short">PCGS</span>
        <span class="long">Pemberly College Graduates Society</span>
      </div>
    </header>
    <p class="brand-club">Pemberly College Graduates Society of Atlanta</p>

    <div class="stamp-box" aria-label="Stamp area"></div>
    <div class="divider"></div>

    <section class="events">
      <h1 class="events-title">Upcoming Events</h1>
      <ul class="event-list">
        <li class="event"><span class="event-date">March 14: </span><span class="event-name">General Body Meeting</span></li>
        <li class="event"><span class="event-date">April 8-12: </span><span class="event-name">Springbreak Bus Trip<br>to Pemberly College</span></li>
        <li class="event"><span class="event-date">August 15: </span><span class="event-name">FalconJam</span></li>
      </ul>
    </section>

    <div class="address-lines" aria-label="Mailing address">
      <div class="address-line"></div>
      <div class="address-line"></div>
      <div class="address-line"></div>
      <div class="address-line"></div>
    </div>
  </main>
</body>
</html>
```